Gestatlung flyer (2 pages) format selectable, based accompanying templates (logo, text) Projektflyer "intercultural cooking class with asylum seekers' data Friday evenings 17. 03 / 24.03 / 31.03 / 07.04 / Time: 18:30 Location: KL Marbeck St. Gallen Title: Intercultural cooking class with asylum seekers text: cooking course is run by asylum seekers. Cooking together, outlandish specialties, exciting conversations Registration: until 24h before the event costs: Expenses participation at its discretion Logos: Pepper Grove, Stifung Valmora. The logos should be listed as the sender and do not dominate the flyer. --------- Just be creative, everything is permitted and desired. The goal is that we make as many people as possible aware of this flyer. The flyers are distributed and the target audience is young adults. Dr Flyer should be correspondingly Modern, Emotianal and sales driven (screaming). Strong Typo, clearly legible and the content clearly structured. The shape of the flyer is free! In total we leave you as much creative freedom as possible. I am looking forward to the many great suggestions and am very excited about the results.

Target Market(s)

Young adults

Font styles to use
Serif
Sans Serif
Script

Requirements
Must have
• Textunterstüzung by appropriate images. Friendly design, bright colors. Very easy to read, weighted Title entsrprechend.
Nice to have
• Emotional Cook image or illustration
Should not have
• No picture with white and dark-skinned people.

```html
<!DOCTYPE html>
<html lang="de">
<head>
<meta charset="utf-8">
<title>Interkultureller Kochkurs mit Asylsuchenden</title>
<link href="https://fonts.googleapis.com/css2?family=Questrial&family=Jost:wght@600;700&family=Allura&display=swap" rel="stylesheet">
<style>
  :root {
    --orange: #e8863a;
    --white: #ffffff;
    --ink: #1b1a19;
    --band: #202020;
    --board: #161616;
    --silver: #cfd2d4;
    --photo-dark: #1a120c;
    --photo-warm: #7a4a26;
  }
  * { margin: 0; padding: 0; box-sizing: border-box; }
  html, body { width: 950px; height: 1200px; overflow: hidden; background: #e6e6e6; }
  .flyer {
    position: relative; width: 950px; height: 1200px;
    background: var(--ink); color: var(--white);
    font-family: "Questrial", sans-serif; overflow: hidden;
  }
  .hero-photo {
    position: absolute; left: 0; top: 0; width: 950px; height: 620px;
    background:
      radial-gradient(ellipse 45% 55% at 28% 35%, rgba(214,170,130,.55), transparent 70%),
      radial-gradient(ellipse 60% 40% at 75% 80%, rgba(190,110,50,.5), transparent 70%),
      linear-gradient(180deg, var(--photo-dark) 0%, var(--photo-warm) 70%, #2a1a10 100%);
  }
  .title { position: absolute; right: 70px; top: 56px; text-align: right; }
  .title-lead { color: var(--orange); font-size: 44px; letter-spacing: 1px; }
  .title-main {
    font-family: "Allura", cursive; font-size: 140px; line-height: 0.85; font-weight: 400;
    margin-top: -4px; text-shadow: 0 4px 10px rgba(0,0,0,.5);
  }
  .title-sub { color: var(--orange); font-size: 48px; letter-spacing: 1px; margin-top: 6px; }
  .title-rule { width: 180px; height: 5px; background: var(--white); margin: 14px 0 0 auto; }
  .intro {
    position: absolute; right: 60px; top: 405px; text-align: right;
    font-size: 27px; line-height: 1.45; letter-spacing: .5px;
  }
  .schedule {
    position: absolute; left: 0; top: 620px; width: 950px; height: 280px;
    background: var(--band); text-align: center;
  }
  .schedule-day { font-family: "Jost", sans-serif; font-weight: 700; font-size: 46px; line-height: 1.2; margin-top: 22px; }
  .schedule-dates {
    font-family: "Jost", sans-serif; font-weight: 600; font-size: 50px; line-height: 1.2;
    color: var(--orange); margin-top: 4px;
  }
  .schedule-dates .sep { color: var(--white); margin: 0 12px; }
  .schedule-rule { width: 440px; height: 2px; background: var(--orange); margin: 14px auto 0; }
  .schedule-info { font-size: 32px; line-height: 1.4; margin-top: 10px; }
  .tool { position: absolute; border-radius: 6px; }
  .tool-knife { left: 36px; top: 700px; width: 52px; height: 180px; background: linear-gradient(180deg, #d6d9db, #3a3a3a); transform: rotate(-14deg); }
  .tool-spatula { right: 36px; top: 632px; width: 44px; height: 120px; background: linear-gradient(180deg, #bdbdbd, #7a4a26); transform: rotate(-40deg); }
  .tool-bowl { right: 18px; top: 790px; width: 118px; height: 92px; background: linear-gradient(135deg, #111 40%, #e3a13a 60%); border-radius: 12px; }
  .divider { position: absolute; left: 0; top: 895px; width: 950px; height: 62px; }
  .signup {
    position: absolute; left: 0; top: 955px; width: 950px; height: 245px;
    background: var(--board); text-align: center;
  }
  .signup-deadline { font-family: "Jost", sans-serif; font-weight: 700; font-size: 40px; line-height: 1.2; color: var(--orange); margin-top: 34px; letter-spacing: 1px; }
  .signup-costs { font-size: 30px; line-height: 1.2; margin-top: 10px; letter-spacing: .5px; }
  .signup-rule { width: 850px; height: 2px; background: var(--orange); margin: 26px auto 0; }
  .senders { display: flex; justify-content: space-between; align-items: center; padding: 20px 50px 0; }
  .sender { font-family: "Questrial", sans-serif; font-size: 36px; color: var(--white); display: flex; align-items: center; gap: 12px; }
  .sender-mark { width: 26px; height: 26px; background: var(--orange); }
</style>
</head>
<body>
<main class="flyer">
  <div class="hero-photo" role="img" aria-label="Dampfender Kochtopf auf einem Herd im warmen Gegenlicht"></div>

  <header class="title">
    <p class="title-lead">Interkultureller</p>
    <h1 class="title-main">Kochkurs</h1>
    <p class="title-sub">mit Asylsuchenden</p>
    <div class="title-rule"></div>
  </header>

  <p class="intro">Kochkurs wird von<br>Asylsuchenden geleitet.<br>Gemeinsames Kochen,<br>fremdländische Spezialiäten,<br>spannende Gespräche</p>

  <section class="schedule">
    <h2 class="schedule-day">Freitag Abende</h2>
    <p class="schedule-dates">17.03<span class="sep">|</span>24.03<span class="sep">|</span>31.03<span class="sep">|</span>07.04</p>
    <div class="schedule-rule"></div>
    <p class="schedule-info">Zeit: 18.30h<br>Ort: KL Marbeck St.Gallen</p>
  </section>

  <div class="tool tool-knife" role="img" aria-label="Küchenmesser"></div>
  <div class="tool tool-spatula" role="img" aria-label="Pfannenwender"></div>
  <div class="tool tool-bowl" role="img" aria-label="Schale mit Chilischoten auf kariertem Tuch"></div>

  <section class="signup">
    <p class="signup-deadline">BIS 24H VOR DEM ANLASS</p>
    <p class="signup-costs">Unkostenbeteiligung nach eigenem Ermessen</p>
    <div class="signup-rule"></div>
    <footer class="senders">
      <span class="sender"><span class="sender-mark"></span>Stifung Valmora</span>
      <span class="sender">Pepper Grove</span>
    </footer>
  </section>

  <svg class="divider" viewBox="0 0 950 62" aria-hidden="true">
    <polygon points="0,10 475,55 950,0 950,62 0,62" fill="var(--board)"/>
    <polyline points="0,10 475,55 950,0" fill="none" stroke="var(--silver)" stroke-width="6"/>
  </svg>
</main>
</body>
</html>
```